2 Elite Law Firms on 1 double-sided monument Sign

The original story: 2 separate law firms already have their own perfect individual sign monuments, one for each firm. However, we must now combine them into 1 monument.

Target Market(s)

high-end clientele

Industry/Entity Type

Legal

Requirements
Must have
• Sleek, equal representation of both firms.

```html
<!DOCTYPE html>
<html lang="en">
<head>
<meta charset="utf-8">
<title>Whitford &amp; Associates and Seawell Lawgroup Monument Sign</title>
<link rel="stylesheet" href="https://fonts.googleapis.com/css2?family=Cinzel:wght@400;500&family=Noto+Serif:wght@500&display=swap">
<style>
  :root {
    --page: #fefefe;
    --walnut: #542915;
    --cobalt: #22419b;
    --ivory: #ffffff;
  }
  * { margin: 0; padding: 0; box-sizing: border-box; }
  html, body {
    width: 1200px;
    height: 871px;
    overflow: hidden;
    background: var(--page);
  }
  .canvas {
    position: relative;
    width: 1200px;
    height: 871px;
  }
  .face {
    position: absolute;
    top: 263px;
    display: flex;
    flex-direction: column;
  }
  .face--main { left: 195px; width: 683px; }
  .face--edge { left: 895px; width: 119px; }
  .band {
    position: relative;
    color: var(--ivory);
  }
  .band--walnut { background: var(--walnut); height: 201px; }
  .band--cobalt { background: var(--cobalt); height: 150px; }

  .firm-name {
    position: absolute;
    left: 0;
    right: 0;
    font-family: "Cinzel", serif;
    font-weight: 400;
    text-align: center;
    line-height: 1;
    color: var(--ivory);
  }
  .firm-name__line {
    display: block;
    font-size: 66px;
    letter-spacing: 3px;
  }
  .firm-name--whitford { top: 27px; padding-left: 90px; }
  .firm-name--whitford .firm-name__line + .firm-name__line { margin-top: -6px; }
  .firm-tagline {
    position: absolute;
    top: 149px;
    left: 0;
    right: 0;
    padding-left: 90px;
    text-align: center;
    font-family: "Cinzel", serif;
    font-size: 24px;
    letter-spacing: 1px;
    color: var(--ivory);
  }
  .firm-name--seawell { top: 45px; }
  .firm-name--seawell .firm-name__line { font-size: 44px; letter-spacing: 2px; }
  .firm-name--seawell .firm-name__sub {
    display: block;
    margin-top: 8px;
    font-size: 15px;
    letter-spacing: 9px;
  }

  .edge-mark {
    position: absolute;
    left: 0;
    right: 0;
    text-align: center;
    font-family: "Cinzel", serif;
    color: var(--ivory);
    line-height: 1;
  }
  .edge-mark--walnut { top: 22px; font-size: 40px; }
  .edge-mark--cobalt { top: 22px; font-size: 26px; letter-spacing: 1px; }
  .suite-number {
    position: absolute;
    left: 0;
    right: 0;
    text-align: center;
    font-family: "Noto Serif", serif;
    font-weight: 500;
    font-size: 46px;
    letter-spacing: 2px;
    color: var(--ivory);
    line-height: 1;
  }
  .band--walnut .suite-number { top: 94px; }
  .band--cobalt .suite-number { top: 89px; }
</style>
</head>
<body>
  <main class="canvas">
    <section class="face face--main" aria-label="Main sign face">
      <div class="band band--walnut">
        <h1 class="firm-name firm-name--whitford">
          <span class="firm-name__line">WHITFORD</span>
          <span class="firm-name__line">&amp; ASSOCIATES</span>
        </h1>
        <p class="firm-tagline">ATTORNEYS AT LAW</p>
      </div>
      <div class="band band--cobalt">
        <h2 class="firm-name firm-name--seawell">
          <span class="firm-name__line">SEAWELL</span>
          <span class="firm-name__sub">LAWGROUP</span>
        </h2>
      </div>
    </section>

    <section class="face face--edge" aria-label="Suite directory">
      <div class="band band--walnut">
        <p class="edge-mark edge-mark--walnut">W&amp;A</p>
        <p class="suite-number">717</p>
      </div>
      <div class="band band--cobalt">
        <p class="edge-mark edge-mark--cobalt">SEAWELL</p>
        <p class="suite-number">715</p>
      </div>
    </section>
  </main>
</body>
</html>
```